Business Card for Fashion House

We need a business card design for our personalize fashion service for our customers. the business card should reflect reliability, luxury and creativity.
The brand Gravetto is extracted from "Graceful Vetto"; Gravetto provides fashion designs sprinkled with luxury and style tailored for our elite clients character profile.
Gravetto is created for those who embody class and elegance with a passion for style.
Target Market(s)
Affluent Customers
Industry/Entity Type
Fashion
Contact Information for Business Card
Rania Bou Khalil
Fashion Designer
Telephone: +971 5550123
Mobile +971 555987
Emal q@z.com
Website www.gravetto-example.com
Social Media Youtube g+ Facebook Instagram Pin /gravetto
Font styles to use
Other font styles liked:
- Audrey provided
Look and feel
Each slider illustrates characteristics of the customer's brand and the style your logo design should communicate.

```html
<!DOCTYPE html>
<html lang="en">
<head>
<meta charset="utf-8">
<title>Gravetto — Business Card</title>
<link href="https://fonts.googleapis.com/css2?family=Open+Sans:wght@300;400&display=swap" rel="stylesheet">
<style>
  :root {
    --canvas: #ecebe8;
    --paper: #ffffff;
    --ink: #231f1f;
    --ink-soft: #3a3535;
    --charcoal: #302a29;
    --on-dark: #f4f2ef;
    --shadow: rgba(0,0,0,0.14);
  }
  * { margin: 0; padding: 0; box-sizing: border-box; }
  html, body { width: 1200px; height: 1200px; overflow: hidden; }
  body {
    background: var(--canvas);
    font-family: "Open Sans", Arial, sans-serif;
    display: flex; flex-direction: column; align-items: center; justify-content: center;
    gap: 70px;
  }
  .card {
    position: relative;
    width: 840px; height: 480px;
    box-shadow: 0 14px 30px var(--shadow);
  }
  .card--front { background: var(--paper); color: var(--ink); }
  .card--back { background: var(--charcoal); color: var(--on-dark); }

  .brand { position: absolute; display: flex; flex-direction: column; align-items: center; }
  .brand__dot {
    width: 92px; height: 92px; border-radius: 50%;
    border: 3px solid currentColor; margin-bottom: 42px;
  }
  .brand__name {
    font-weight: 300; font-size: 44px; letter-spacing: 0.42em;
    text-transform: uppercase; margin-right: -0.42em; line-height: 1;
  }
  .card--front .brand { left: 60px; top: 120px; width: 380px; }
  .card--back .brand { left: 0; right: 0; top: 120px; }

  .divider {
    position: absolute; left: 452px; top: 80px; width: 1.5px; height: 250px;
    background: var(--ink);
  }
  .person { position: absolute; left: 474px; top: 78px; }
  .person__name { font-size: 30px; font-weight: 400; line-height: 1.15; }
  .person__title { font-size: 17px; font-weight: 400; color: var(--ink-soft); margin-bottom: 26px; }
  .contacts { list-style: none; font-size: 16px; line-height: 1.6; color: var(--ink-soft); }
  .contacts li { display: flex; align-items: center; gap: 10px; }
  .contacts svg { width: 16px; height: 16px; flex: none; }

  .social {
    position: absolute; right: 46px; bottom: 40px;
    font-size: 16px; font-weight: 400; letter-spacing: 0.04em;
  }
</style>
</head>
<body>

<section class="card card--front" aria-label="Business card front">
  <div class="brand">
    <span class="brand__dot" aria-hidden="true"></span>
    <span class="brand__name">Gravetto</span>
  </div>
  <span class="divider" aria-hidden="true"></span>
  <div class="person">
    <p class="person__name">Rania Bou Khalil</p>
    <p class="person__title">Fashion Designer</p>
    <ul class="contacts">
      <li>
        <svg viewBox="0 0 16 16" aria-hidden="true"><path fill="currentColor" d="M3.2 1.5l2.4 2.6-1.2 1.7c.9 2 2.4 3.6 4.4 4.6l1.6-1.2 2.8 2.3-1.4 2.3C7 13.6 2.4 9 1.4 3.2z"/></svg>
        +971 5550123
      </li>
      <li>
        <svg viewBox="0 0 16 16" aria-hidden="true"><rect x="4" y="1" width="8" height="14" rx="1.5" fill="currentColor"/><rect x="5.5" y="3" width="5" height="8" fill="#fff"/></svg>
        +971 555987
      </li>
      <li>
        <svg viewBox="0 0 16 16" aria-hidden="true"><rect x="1" y="3" width="14" height="10" fill="currentColor"/><path d="M1.5 3.5L8 9l6.5-5.5" fill="none" stroke="#fff" stroke-width="1.2"/></svg>
        q@z.com
      </li>
      <li>
        <svg viewBox="0 0 16 16" aria-hidden="true"><circle cx="8" cy="8" r="7" fill="currentColor"/><g fill="none" stroke="#fff" stroke-width="1"><ellipse cx="8" cy="8" rx="3" ry="6.5"/><path d="M1.5 8h13M2.5 4.8h11M2.5 11.2h11"/></g></svg>
        www.gravetto-example.com
      </li>
    </ul>
  </div>
  <p class="social">/gravetto</p>
</section>

<section class="card card--back" aria-label="Business card back">
  <div class="brand">
    <span class="brand__dot" aria-hidden="true"></span>
    <span class="brand__name">Gravetto</span>
  </div>
  <p class="social">/gravetto</p>
</section>

</body>
</html>
```